Illustration Design Project

I have an existing illustration I have written up, I need it professionally redone, perhaps as an infographic or new design from the current layout.

Pls plan for a few edits and revisions.

I will need it large enough to be made into a wall poster size.

```html
<!DOCTYPE html>
<html lang="en">
<head>
<meta charset="utf-8">
<title>Accountable vs. Complacency</title>
<link rel="stylesheet" href="https://fonts.googleapis.com/css2?family=Cinzel:wght@400;700&family=Patrick+Hand&family=Arimo:ital@1&display=swap">
<style>
  :root {
    --frame-dark: #17120d;
    --frame-gold: #b58a3c;
    --parchment-light: #f3d79a;
    --parchment-mid: #e2b769;
    --parchment-edge: #c48d3a;
    --ink: #2b2014;
    --arrow: #e9823b;
    --arrow-light: #fbd3b0;
    --badge-ring: #1c1c1c;
    --badge-light: #e9ecdf;
    --badge-dark: #6e7264;
  }
  * { margin: 0; padding: 0; box-sizing: border-box; }
  html, body { width: 900px; height: 1200px; overflow: hidden; background: var(--frame-dark); }
  .poster { position: relative; width: 900px; height: 1200px; overflow: hidden; }
  .poster-art { position: absolute; inset: 0; }
  .subtitle {
    position: absolute; top: 43px; left: 0; width: 900px; text-align: center;
    font: italic 10.5px "Arimo", sans-serif; color: #111;
  }
  .pole-title {
    position: absolute; left: 0; width: 900px; text-align: center;
    font: 400 40px/1 "Cinzel", serif; color: var(--ink);
  }
  .pole-title span { border-bottom: 2px solid var(--ink); padding: 0 2px 1px; }
  .pole-title.accountable { top: 72px; }
  .pole-title.victim { top: 1102px; }
  .step { position: absolute; left: 0; width: 900px; height: 0; }
  .step-label {
    position: absolute; right: calc(900px - var(--x) + 26px); transform: translateY(-50%);
    font: 400 21px/1.2 "Cinzel", serif; color: var(--ink); text-align: right; white-space: nowrap;
  }
  .step-quote {
    position: absolute; left: calc(var(--x) + 26px); transform: translateY(-50%);
    font: 400 18px/1.15 "Patrick Hand", cursive; color: var(--ink); white-space: nowrap;
    letter-spacing: 0.5px;
  }
  .step-quote.wrap { transform: translateY(-14px); }
  .life-happens {
    position: absolute; left: 0; top: 560px; width: 900px; text-align: center;
    font: 400 52px/0.86 "Cinzel", serif; color: #fff; letter-spacing: 1px;
    -webkit-text-stroke: 1.2px #1d1d1d; text-shadow: 0 2px 4px rgba(0,0,0,.6);
  }
</style>
</head>
<body>
<main class="poster">
  <svg class="poster-art" width="900" height="1200" viewBox="0 0 900 1200">
    <defs>
      <radialGradient id="frame-fill" cx="50%" cy="50%" r="75%">
        <stop offset="0.55" stop-color="#3a2b18"/>
        <stop offset="0.8" stop-color="#8a6a30"/>
        <stop offset="1" stop-color="var(--frame-dark)"/>
      </radialGradient>
      <radialGradient id="parchment" cx="50%" cy="42%" r="60%">
        <stop offset="0" stop-color="var(--parchment-light)"/>
        <stop offset="0.65" stop-color="var(--parchment-mid)"/>
        <stop offset="1" stop-color="var(--parchment-edge)"/>
      </radialGradient>
      <radialGradient id="badge" cx="50%" cy="40%" r="60%">
        <stop offset="0" stop-color="var(--badge-light)"/>
        <stop offset="1" stop-color="var(--badge-dark)"/>
      </radialGradient>
      <radialGradient id="marker" cx="45%" cy="35%" r="65%">
        <stop offset="0" stop-color="#fff"/>
        <stop offset="0.55" stop-color="var(--arrow-light)"/>
        <stop offset="1" stop-color="var(--arrow)"/>
      </radialGradient>
    </defs>

    <rect class="frame" width="900" height="1200" fill="url(#frame-fill)" role="img" aria-label="Ornamental black scrollwork frame on gold"/>
    <ellipse class="parchment" cx="450" cy="600" rx="442" ry="596" fill="url(#parchment)"/>

    <g class="arrow" fill="none" stroke="var(--arrow)" stroke-width="18" stroke-linecap="butt">
      <path d="M447 535 C452 500 440 430 444 400 S462 300 459 260 S456 190 455 155"/>
      <path d="M454 680 C450 720 452 760 447 805 S458 900 461 940 S462 1010 458 1045"/>
    </g>
    <polygon points="420,160 455,122 490,160" fill="var(--arrow)"/>
    <polygon points="424,1040 458,1078 492,1040" fill="var(--arrow)"/>

    <ellipse cx="450" cy="600" rx="194" ry="86" fill="var(--badge-ring)"/>
    <ellipse cx="450" cy="600" rx="176" ry="72" fill="url(#badge)" role="img" aria-label="Swirl ornament behind the title"/>

    <g class="markers" stroke="var(--arrow)" stroke-width="2" fill="url(#marker)">
      <circle cx="458" cy="211" r="21"/>
      <circle cx="459" cy="275" r="21"/>
      <circle cx="450" cy="341" r="21"/>
      <circle cx="442" cy="403" r="21"/>
      <circle cx="449" cy="463" r="21"/>
      <circle cx="454" cy="743" r="21"/>
      <circle cx="445" cy="809" r="21"/>
      <circle cx="452" cy="875" r="21"/>
      <circle cx="461" cy="932" r="21"/>
      <circle cx="462" cy="996" r="21"/>
    </g>
    <g class="marker-numbers" font-family="Cinzel, serif" font-weight="700" font-size="30" fill="#111" text-anchor="middle" dominant-baseline="central">
      <text x="458" y="212">5</text>
      <text x="459" y="276">4</text>
      <text x="450" y="342">3</text>
      <text x="442" y="404">2</text>
      <text x="449" y="464">1</text>
      <text x="454" y="744">1</text>
      <text x="445" y="810">2</text>
      <text x="452" y="876">3</text>
      <text x="461" y="933">4</text>
      <text x="462" y="997">5</text>
    </g>
  </svg>

  <p class="subtitle">Accountable vs. Complacency</p>
  <h1 class="pole-title accountable"><span>Accountable</span></h1>

  <div class="step" style="top:211px;--x:458px"><span class="step-label">Gets on with it</span><span class="step-quote">“ O.K. ,let’s do it ! ”</span></div>
  <div class="step" style="top:275px;--x:459px"><span class="step-label">Fins Solution</span><span class="step-quote">“ What can I do ? ”</span></div>
  <div class="step" style="top:341px;--x:450px"><span class="step-label">Owns it</span><span class="step-quote">“ If it’s to be, it’s up to me ! ”</span></div>
  <div class="step" style="top:415px;--x:442px"><span class="step-label">Acknowledges<br>Reality</span></div>
  <div class="step" style="top:401px;--x:442px"><span class="step-quote">“ This is the way it is. ”</span></div>
  <div class="step" style="top:463px;--x:449px"><span class="step-label">Seeks Reality</span><span class="step-quote">“ What’s happening ? ”</span></div>

  <div class="life-happens">LIFE<br>HAPPENS</div>

  <div class="step" style="top:743px;--x:454px"><span class="step-label">Avoids Reality</span><span class="step-quote">“ Ask no questions. ”</span></div>
  <div class="step" style="top:811px;--x:445px"><span class="step-label">Fights Reality</span><span class="step-quote">“ That’s not how I see it. ”</span></div>
  <div class="step" style="top:876px;--x:452px"><span class="step-label">Blames</span><span class="step-quote wrap">“ If everyone would just<br>&nbsp;&nbsp;do their job ! ”</span></div>
  <div class="step" style="top:943px;--x:461px"><span class="step-label">Personal<br>Excuses</span></div>
  <div class="step" style="top:928px;--x:461px"><span class="step-quote">“ It’s not my job. ”</span></div>
  <div class="step" style="top:996px;--x:462px"><span class="step-label">Waits : Hopes</span><span class="step-quote wrap">“ If it was meant to be,<br>&nbsp;&nbsp;it’ll happen. ”</span></div>

  <h2 class="pole-title victim"><span>Victim</span></h2>
</main>
</body>
</html>
```